Bref créative
Biz Card for a Professional Organizer
Dana Kowalt
Cutting-Edge
Room Clearing Maestro
Serving the Bay Area
info@42plumova.com
www.42plumova.com
I'd like a clean design, possibly going vertical instead of the traditional horizontal-UNLESS it is just going to look better going horizontal.
I'm open to suggestions here. I also have black and white versions of my logo if that would work well here...
black version of logo
reverse version of logo
color version

```html
<!DOCTYPE html>
<html lang="en">
<head>
<meta charset="utf-8">
<title>Dana Kowalt – Business Card</title>
<link rel="stylesheet" href="https://fonts.googleapis.com/css2?family=Open+Sans:wght@400;600&display=swap">
<style>
  :root {
    --paper: #ffffff;
    --brand-blue: #2f7e9e;
    --band-brown: #7b5b44;
    --band-blue: #4f9db3;
    --text-light: #ffffff;
    --text-soft: #f1e9e1;
  }
  * { margin: 0; padding: 0; box-sizing: border-box; }
  html, body {
    width: 1200px;
    height: 684px;
    overflow: hidden;
    background: var(--paper);
  }
  .card {
    position: relative;
    width: 1200px;
    height: 684px;
    font-family: "Open Sans", Arial, sans-serif;
    background: var(--paper);
  }
  .brand {
    position: absolute;
    top: 0;
    left: 0;
    width: 100%;
    height: 378px;
    display: flex;
    align-items: center;
    justify-content: center;
    gap: 22px;
  }
  .brand-dot {
    width: 34px;
    height: 34px;
    border-radius: 50%;
    background: var(--brand-blue);
  }
  .brand-name {
    font-size: 78px;
    font-weight: 600;
    color: var(--brand-blue);
    letter-spacing: 1px;
  }
  .identity-band {
    position: absolute;
    top: 378px;
    left: 0;
    width: 100%;
    height: 142px;
    background: var(--band-brown);
    text-align: center;
    color: var(--text-light);
  }
  .identity {
    margin-top: 34px;
    font-size: 31px;
    font-weight: 600;
  }
  .identity .divider { font-weight: 400; margin: 0 10px; }
  .identity .role { font-weight: 400; font-size: 25px; }
  .service-area {
    margin-top: 10px;
    font-size: 21px;
    color: var(--text-soft);
  }
  .contact-band {
    position: absolute;
    top: 520px;
    left: 0;
    width: 100%;
    height: 164px;
    background: var(--band-blue);
    color: var(--text-light);
  }
  .contact {
    margin: 34px 0 0 64px;
    font-size: 21px;
  }
  .contact .label { font-weight: 600; }
  .contact .sep { margin: 0 10px; }
</style>
</head>
<body>
  <div class="card">
    <header class="brand">
      <span class="brand-dot"></span>
      <span class="brand-name">42 Plumova</span>
    </header>

    <section class="identity-band">
      <p class="identity">Dana Kowalt<span class="divider">/</span><span class="role">Room Clearing Maestro</span></p>
      <p class="service-area">Serving the Bay Area</p>
    </section>

    <footer class="contact-band">
      <p class="contact">
        <span class="label">P:</span> (555) 014-2738<span class="sep">|</span>
        <span class="label">E:</span> info@42plumova.com<span class="sep">|</span>
        <span class="label">W:</span> www.42plumova.com
      </p>
    </footer>
  </div>
</body>
</html>
```